Talvane Companies Business Card Design

We need a new business card for our Private Equity Real Estate Development firm, “Talvane” and our EB-5 regional center “Moorfield Regional Center” on one card. We prefer a design that is simple, elegant, and represents the luxury products we design and build as well as the financial security and stability our successful history has produced. We are an industry leader in our field and 3rd generation family business that has evolved into an institutional quality investment platform. Considered design size is standard business card dimensions (3.5 x 2 inches with an additional 1/8 inch space for design elements or backgrounds that extend beyond the finished size of your piece.

Target Market(s)

• High net worth individuals
• Highly skilled technical workers and physicians in the US seeking investment-based immigration opportunities
• Sophisticated private equity investors
• Intermediary partners include domestic attorneys and investment brokers, as well as international agent networks
• US real estate developers

Industry/Entity Type

Finance

Contact Information for Business Card

(Providing placeholder info for personal information, please design for longer character spaces, longer names and addresses etc..)
• Logo for Talvane
• Logo for Moorfield Regional Center
• Full name: Dorian Talvane
• Job title: CEO
• Email address: dtalvane@talvanecompanies.example
• Cell phone number: +1.555.318.4476
• Office number +1.555.240.6185
• Office address: Quillan Court 5, 4817 Vista Ardell, Larkmere, Westvale.
• Website: www.talvanecompanies.example

Font styles to use
Serif
Sans Serif

Colors
ec1f27
ffffff
000000

Requirements
Must have
• • Logo for Talvane
• • Logo for Moorfield Regional Center
• - Use rounded corners
• (See .ai file included for logos)
Nice to have
• • Simple, elegant design
• • Aesthetically compatible with our website design (www.talvanecompanies.example)
• • Color palette including but not limited to white, black, and red (as per logos)
Should not have
• - Not too much red color
• - Do not stack both logos on top of each other

```html
<!DOCTYPE html>
<html lang="en">
<head>
<meta charset="utf-8">
<title>Talvane Companies Business Card</title>
<link rel="stylesheet" href="https://fonts.googleapis.com/css2?family=Open+Sans:wght@400;600&display=swap">
<style>
  :root {
    --page-bg: #1c1c1c;
    --card-bg: #272727;
    --text-white: #ffffff;
    --text-soft: #e6e6e6;
    --brand-red: #a8192e;
    --card-radius: 34px;
  }
  * { margin: 0; padding: 0; box-sizing: border-box; }
  html, body {
    width: 1200px;
    height: 1200px;
    overflow: hidden;
    background: var(--page-bg);
    font-family: "Open Sans", Arial, sans-serif;
  }
  .card {
    position: absolute;
    left: 194px;
    width: 878px;
    height: 501px;
    background: var(--card-bg);
    border-radius: var(--card-radius);
  }
  .card--front { top: 35px; }
  .card--back { top: 664px; }

  .wordmark {
    position: absolute;
    display: flex;
    align-items: center;
    gap: 14px;
    font-weight: 600;
    letter-spacing: 0.04em;
    text-transform: uppercase;
    white-space: nowrap;
  }
  .wordmark__square {
    width: 22px;
    height: 22px;
    flex: none;
  }
  .wordmark--capital {
    left: 38px;
    top: 62px;
    font-size: 44px;
    color: var(--text-white);
  }
  .wordmark--capital .wordmark__square { background: var(--text-white); }
  .wordmark--center {
    right: 40px;
    bottom: 56px;
    font-size: 36px;
    color: var(--brand-red);
  }
  .wordmark--center .wordmark__square { background: var(--brand-red); }

  .person {
    position: absolute;
    left: 36px;
    top: 190px;
    color: var(--text-white);
  }
  .person__name {
    font-size: 34px;
    font-weight: 600;
    line-height: 1.1;
  }
  .person__title {
    font-size: 19px;
    margin-top: 4px;
    margin-left: 3px;
    color: var(--text-soft);
  }
  .address {
    position: absolute;
    left: 37px;
    top: 279px;
    font-size: 19px;
    line-height: 21px;
    color: var(--text-soft);
    font-style: normal;
  }
  .contact-list {
    position: absolute;
    left: 40px;
    top: 342px;
    list-style: none;
    color: var(--text-soft);
    font-size: 18px;
  }
  .contact-list__item {
    display: flex;
    align-items: center;
    height: 29px;
  }
  .contact-list__icon {
    width: 20px;
    height: 20px;
    margin-right: 22px;
    flex: none;
  }
</style>
</head>
<body>

<section class="card card--front" aria-label="Card front">
  <div class="wordmark wordmark--capital">
    <span class="wordmark__square"></span>
    <span class="wordmark__name">Talvane Capital</span>
  </div>

  <div class="person">
    <h1 class="person__name">Dorian Talvane</h1>
    <p class="person__title">CEO</p>
  </div>

  <address class="address">
    Quillan Court 5, 4817<br>
    Vista Ardell Larkmere, Westvale
  </address>

  <ul class="contact-list">
    <li class="contact-list__item">
      <svg class="contact-list__icon" viewBox="0 0 20 20" aria-hidden="true">
        <rect x="5" y="1" width="10" height="18" rx="2" fill="none" stroke="#fff" stroke-width="1.6"/>
        <circle cx="10" cy="16" r="1" fill="#fff"/>
      </svg>
      +1555 - 318 - 4476
    </li>
    <li class="contact-list__item">
      <svg class="contact-list__icon" viewBox="0 0 20 20" aria-hidden="true">
        <path d="M2 8 C2 4 18 4 18 8 L15 9 L14 7 L6 7 L5 9 Z" fill="#fff"/>
        <path d="M5 10 L15 10 L17 16 L3 16 Z" fill="#fff"/>
      </svg>
      +1555 - 240 - 6185
    </li>
    <li class="contact-list__item">
      <svg class="contact-list__icon" viewBox="0 0 20 20" aria-hidden="true">
        <rect x="1.5" y="4" width="17" height="12" fill="none" stroke="#fff" stroke-width="1.6"/>
        <path d="M1.5 4 L10 11 L18.5 4" fill="none" stroke="#fff" stroke-width="1.6"/>
      </svg>
      dtalvane@talvanecompanies.example
    </li>
    <li class="contact-list__item">
      <svg class="contact-list__icon" viewBox="0 0 20 20" aria-hidden="true">
        <circle cx="10" cy="10" r="8" fill="none" stroke="#fff" stroke-width="1.3"/>
        <ellipse cx="10" cy="10" rx="3.5" ry="8" fill="none" stroke="#fff" stroke-width="1.1"/>
        <path d="M2 10 H18 M3.5 6 H16.5 M3.5 14 H16.5" stroke="#fff" stroke-width="1.1"/>
      </svg>
      www.talvanecompanies.example
    </li>
  </ul>
</section>

<section class="card card--back" aria-label="Card back">
  <div class="wordmark wordmark--center">
    <span class="wordmark__square"></span>
    <span class="wordmark__name">Moorfield Regional Center</span>
  </div>
</section>

</body>
</html>
```